Commercial Auto Insurance Application and Commercial Property Insurance Application

Hi I need a fillable application for my business to send to potential clients for Commercial Auto Insurance and Commercial Property Insurance. I have attached an example application I currently use for another line of insurance.
Commercial Auto Insurance Application
On the first page I would need the following:
- Business Name: (fill in area for text)
- Effective Date: (fill in area for text)
- How do you structure your business? (Check box for “Sole Proprietor”, “Partnership”, “Corporation”, “LLC”)
- Contact Name: (fill in area for text) / Phone Number: (fill in area for text) / Contact Email (fill in area for text)
- Mailing address: (fill in area for text)
- Garaging location: (fill in area for text)
- Owner Name: (fill in area for text)
- Description of Operations: (fill in area for text)
- How long has the operation been in business? (fill in area for text)
- How many years of experience does your management have in the truck/transportation industry? (fill in area for text)
Coverages
Liability Combined Single Limit: ($1,000,000 (checkbox) / $500,000 (checkbox / $300,000 (checkbox) / Other: (fill in area for text)
Uninsured Motorist CSL: (fill in area for text) (checkbox for “Rejected”)
Medical Payments: (fill in area for text)
Physical Damage: (fill in area for text) (checkbox for Rejected)
Liability Deducible: ($500 checkbox, $1,000 checkbox, $2,500 checkbox, $5,000 checkbox)
Physical Damage Deductible: ($500 checkbox, $1,000 checkbox, $2,500 checkbox, $5,000 checkbox)
Driving radius: (fill in area for text)
How many years have you had your own continuous commercial auto insurance coverage for the current business name? (fill in area for text)
Do any of your vehicles travel across state lines? Yes (checkbox)/ No (checkbox)
If yes, please list all states in which vehicles operate: (fill in area for text)
What is the maximum radius traveled for your customer's business?
0-25 miles (checkbox)
26-50 miles (checkbox)
51-75 miles (checkbox)
76-100 miles (checkbox)
101-150 miles (checkbox)
151-200 miles (checkbox)
201-300 miles (checkbox)
300+ miles (checkbox)
Would you like physical damage coverage for this vehicle? (should be for each vehicle listed)
On the 2nd page of the application I would need the following:
I would need to have it where people can fill in the vehicle information such as VIN:, Year:, Make:, Model:, Type of Vehicle:, Trailers:, Value:
I would also need to have it where people can fill in the drivers with their driver info including Name:, DOB:, DL #:, DL State:, Class of License:, Married: Yes/No, Number of years driving similar vehicle:
Please make it where you can fill in 20 vehicle's information and 20 driver's info.
For the 2nd Application I would need one for Property Insurance
On the Commercial Property Application I would need the following:
- Building Address: (fill in area for text)
- Building Description: (fill in area for text)
- Building Amount: $(fill in area for text)
- Business Personal Property Amount: $ (fill in area for text) (checkbox for Not Needed)
- Building Sq Ft: (fill in area for text)
- Total Area Sq Ft: (fill in area for text)
- Building Construction Type: Wood Frame (checkbox), Steel (checkbox), Fire Resistive (checkbox), Non-Combustible (checkbox), Other (fill in area for text)
- # of stories: (fill in area for text)
- Year Built: (fill in area for text)
- Wiring improvement year: (fill in area for text)
- Roofing improvement year: (fill in area for text)
- Plumbing improvement year: (fill in area for text)
- Heating improvement year: (fill in area for text)
- What is to the right of the building and distance: (fill in area for text)
- What is to the left of the building and distance: (fill in area for text)
- What is in front of the building and distance: (fill in area for text)
- What is behind the building and distance: (fill in area for text)
- Burglar alarm installation and serviced by: (fill in area for text) None (checkbox)
- Does the premises have fire protection? Sprinkler system (checkbox), Fire detection (checkbox), Other: (fill in area for text) None (checkbox)

```html
<!DOCTYPE html>
<html lang="en">
<head>
<meta charset="utf-8">
<title>Application Property Insurance</title>
<link rel="stylesheet" href="https://fonts.googleapis.com/css2?family=Montserrat:wght@700&family=Source+Sans+3:wght@400;600&display=swap">
<style>
  :root {
    --ink: #231f20;
    --brand-navy: #2b3a87;
    --title-blue: #4159a8;
    --paper: #ffffff;
    --rule: 1.5px solid var(--ink);
  }
  * { box-sizing: border-box; margin: 0; padding: 0; }
  html, body { width: 856px; height: 1200px; overflow: hidden; background: var(--paper); }
  body { font-family: "Source Sans 3", "Myriad Pro", sans-serif; color: var(--ink); }
  .sheet { position: relative; width: 856px; height: 1200px; }

  .brand { position: absolute; left: 39px; top: 62px; display: flex; align-items: center; gap: 10px;
    color: var(--brand-navy); font-weight: 600; font-size: 24px; line-height: 1.05; }
  .brand-mark { width: 14px; height: 14px; background: var(--brand-navy); }

  .office { position: absolute; right: 54px; top: 38px; text-align: right; font-size: 15.5px; line-height: 22px; }

  .title { position: absolute; left: 0; right: 0; top: 148px; text-align: center;
    font-family: "Montserrat", sans-serif; font-weight: 700; font-size: 34px; color: var(--title-blue); letter-spacing: 0.2px; padding-left: 8px; }

  .label, .field { position: absolute; height: 47px; display: flex; align-items: center; font-size: 15.5px; white-space: nowrap; }
  .field { border: var(--rule); padding-left: 8px; }
  .field.end { justify-content: flex-end; padding-right: 0; border-right: var(--rule); }

  .choice-row { position: absolute; top: 481px; left: 46px; height: 27px; }
  .choice { position: absolute; top: 0; display: flex; align-items: center; font-size: 15.5px; white-space: nowrap; }
  .checkbox { width: 24px; height: 24px; border: var(--rule); margin-right: 3px; flex: none; }
</style>
</head>
<body>
<main class="sheet">
  <header>
    <div class="brand"><span class="brand-mark"></span><span>Ridgeline<br>Insurance Services</span></div>
    <address class="office" style="font-style:normal">
      Ridgeline Insurance Services<br>
      4820 Cedar Park Ave Suite 310<br>
      Maple Grove, CA 91500<br>
      Tel: (555) 014-2290
    </address>
  </header>

  <h1 class="title">Application Property Insurance</h1>

  <section class="form">
    <div class="label" style="left:37px;top:197px">Business Name:</div>
    <div class="field" style="left:148px;top:197px;width:655px">(fill in area for text)</div>

    <div class="label" style="left:37px;top:244px">Building Address:</div>
    <div class="field" style="left:163px;top:244px;width:640px">(fill in area for text)</div>

    <div class="label" style="left:37px;top:291px">Building Amount: $</div>
    <div class="field" style="left:175px;top:291px;width:628px">(fill in area for text)</div>

    <div class="label" style="left:37px;top:338px">Business Personal Property Amount: $</div>
    <div class="field" style="left:299px;top:338px;width:361px;padding-left:3px">(fill in area for text)</div>
    <div class="field end" style="left:659px;top:338px;width:144px;border-top:none;border-bottom:none;border-left:var(--rule)">Not Needed)</div>

    <div class="label" style="left:37px;top:385px">Building Sq Ft:</div>
    <div class="field" style="left:137px;top:385px;width:242px;padding-left:5px">(fill in area for text)</div>
    <div class="label" style="left:386px;top:385px">Total Area Sq Ft:</div>
    <div class="field" style="left:497px;top:385px;width:307px;padding-left:4px">(fill in area for text)</div>

    <div class="label" style="left:37px;top:432px">Building Construction Type:</div>
    <div class="choice-row">
      <div class="choice" style="left:0"><span class="checkbox"></span>Wood Frame</div>
      <div class="choice" style="left:131px"><span class="checkbox"></span>Steel</div>
      <div class="choice" style="left:207px"><span class="checkbox"></span>Fire Resistive</div>
      <div class="choice" style="left:332px"><span class="checkbox"></span>Non-Combustible</div>
      <div class="choice" style="left:486px;top:3px"><span class="checkbox"></span>Other (fill in area for text)</div>
    </div>

    <div class="label" style="left:37px;top:527px"># of stories</div>
    <div class="field" style="left:112px;top:527px;width:270px;padding-left:6px">(fill in area for text)</div>
    <div class="label" style="left:386px;top:527px">Year Built</div>
    <div class="field" style="left:450px;top:527px;width:354px;padding-left:2px">(fill in area for text)</div>

    <div class="label" style="left:37px;top:574px">Year Wiring Improvement:</div>
    <div class="field" style="left:240px;top:574px;width:563px">(fill in area for text)</div>
    <div class="label" style="left:37px;top:621px">Year Roofing Improvement:</div>
    <div class="field" style="left:240px;top:621px;width:563px">(fill in area for text)</div>
    <div class="label" style="left:37px;top:669px">Year Plumbing Improvement:</div>
    <div class="field" style="left:240px;top:669px;width:563px">(fill in area for text)</div>
    <div class="label" style="left:37px;top:716px">Year Heating Improvement:</div>
    <div class="field" style="left:240px;top:716px;width:563px">(fill in area for text)</div>

    <div class="label" style="left:37px;top:763px">What is to the right of the building and distance:</div>
    <div class="field" style="left:369px;top:763px;width:434px">(fill in area for text)</div>
    <div class="label" style="left:37px;top:810px">What is to the left of the building and distance:</div>
    <div class="field" style="left:369px;top:810px;width:434px">(fill in area for text)</div>
    <div class="label" style="left:37px;top:858px">What is in front of the building and distance:</div>
    <div class="field" style="left:369px;top:858px;width:434px">(fill in area for text)</div>
    <div class="label" style="left:37px;top:905px">What is behind the building and distance:</div>
    <div class="field" style="left:369px;top:905px;width:434px;padding-left:11px">(fill in area for text)</div>
    <div class="label" style="left:37px;top:952px">Burglar alarm installation and serviced by:</div>
    <div class="field" style="left:369px;top:952px;width:434px;padding-left:6px">(fill in area for text)</div>
    <div class="label" style="left:37px;top:1000px">Does Premises have fire protection?</div>
    <div class="field" style="left:368px;top:1000px;width:435px"></div>
  </section>
</main>
</body>
</html>
```